Online tuition webpage design needed

Hi,
We are starting up an online tuition website for non- English speakers wishing to take an QUOLT test.

The webpage must include a place for people to enroll online in the course.
The home page must have:
• room for a logo (coming shortly, blue in colour)
• different packages of online tuition and payvora
• tool bar showing different pages
• perhaps a video, small pictures

This is my site currently:-

www.lingvarotutors.example

as you can see, I am not very sure how to create a website … The large logo is what I would like to use, but I project has not been finalized yet. Please note, I don’t like the logo being that large!

Sites that are similar to what I am doing and like the design of are:

http://www.tesmarilearn.example.au/fees

https://www.brovaskill.example/index.php

http://www.pelgrimtutorkaspar.example.uk/index.html

http://www.quorvanexams.example/

One thing I need is a place for student s to enroll, and if possible, I would like to use quillet to create exercises for students.
Currently, my site is using pagecraftr. My preference is to use quillet for online activities. I am not sure if I can use both.
Thanks in advance

Target Market(s)

people wising to take an QUOLT test (English proficiency test)

Industry/Entity Type

Online

Colors
3276b5
0292cd

Requirements
Must have
• a place for enrollment and admin login for students
quillet
video
talqo, friendwall, chirplo logos
Nice to have
• a booking calender
Should not have
• too much clutter. must be clean and professional looking

```html
<!DOCTYPE html>
<html lang="en">
<head>
<meta charset="utf-8">
<title>QUOLT Online Tuition</title>
<link href="https://fonts.googleapis.com/css2?family=Montserrat:wght@300;400;600;700&family=Open+Sans:ital,wght@0,400;0,600;1,400&display=swap" rel="stylesheet">
<style>
:root{
  --brand:#0292cd;
  --brand-deep:#3276b5;
  --nav:#0aa4ea;
  --nav-active:#0a86c6;
  --sky:#86d1f6;
  --ink:#2b2b2b;
  --text:#555;
  --muted:#7a7a7a;
  --hero-bg:#f3f3f3;
  --band-grey:#f2f2f2;
  --footer:#333;
  --accent:#ee8a12;
  --white:#fff;
}
*{box-sizing:border-box;margin:0;padding:0}
html,body{width:1200px;height:2419px;overflow:hidden}
body{font-family:"Open Sans",Arial,sans-serif;color:var(--text);background:var(--white);position:relative}
section,header,nav,footer{position:absolute;left:0;width:1200px}
.abs{position:absolute}
.heading{font-family:"Montserrat",Arial,sans-serif;font-weight:700;color:var(--ink);text-align:center;letter-spacing:.5px}

/* header */
.site-header{top:0;height:109px}
.logo{left:174px;top:30px;font-family:"Montserrat",Arial,sans-serif;font-weight:700;font-size:32px;color:var(--brand)}
.login-links{right:270px;top:46px;display:flex;gap:22px;white-space:nowrap}
.login-link{font-family:"Montserrat",Arial,sans-serif;font-size:12px;color:#444}
.enrol{left:949px;top:41px;width:74px;height:27px;border-radius:14px;background:var(--brand);color:var(--white);font-family:"Montserrat",Arial,sans-serif;font-weight:600;font-size:13px;text-align:center;line-height:27px}

/* nav */
.main-nav{top:109px;height:48px;background:var(--nav);border-bottom:4px solid #38b9f0}
.main-nav a{position:absolute;top:0;height:44px;line-height:44px;color:var(--white);font-family:"Montserrat",Arial,sans-serif;font-weight:600;font-size:12px;text-decoration:none;transform:translateX(-50%);white-space:nowrap}
.main-nav a.active{background:var(--nav-active);width:70px;text-align:center}

/* hero */
.hero{top:157px;height:460px;background:var(--hero-bg)}
.hero h1{position:absolute;top:46px;width:100%;font-size:34px;line-height:42px;color:#555}
.hero h1 span{color:var(--brand)}
.hero-photo{left:109px;top:158px;width:992px;height:295px;background:linear-gradient(90deg,#e9c9a6 0%,#7fc3b0 25%,#e88c54 45%,#4b5568 70%,#d9b783 100%);border-radius:4px}

/* features */
.features{top:617px;height:332px;background:var(--brand-deep)}
.feature{position:absolute;top:48px;width:240px;text-align:center;transform:translateX(-50%)}
.feature-icon{width:80px;height:80px;margin:0 auto}
.feature h3{margin-top:18px;font-family:"Montserrat",Arial,sans-serif;font-weight:400;font-size:20px;color:var(--white)}
.feature p{margin-top:20px;font-size:11px;line-height:16px;color:#b9d3ee}
.feature .dots{margin-top:14px;color:#cfe0f2;font-size:14px;letter-spacing:3px}

/* packages */
.packages{top:949px;height:435px}
.packages h2{position:absolute;top:42px;width:100%;font-size:31px}
.packages .intro{position:absolute;left:235px;top:96px;width:730px;font-size:11.5px;line-height:17px;text-align:center;color:#444}
.package{position:absolute;top:192px;width:200px;text-align:center;transform:translateX(-50%)}
.package h3{font-family:"Montserrat",Arial,sans-serif;font-weight:400;font-size:20px;color:#333}
.package p{margin:12px auto 0;width:150px;font-size:11px;line-height:16px;color:var(--muted)}
.btn{display:inline-block;margin-top:20px;width:73px;height:29px;line-height:29px;background:var(--brand-deep);color:var(--white);font-size:11px;font-weight:600;border-radius:2px}
.vrule{position:absolute;width:1px;background:#dcdcdc}

/* video */
.video-band{top:1384px;height:460px;background:var(--sky)}
.video-band h2{position:absolute;top:40px;width:100%;font-size:31px}
.video-band .sub{position:absolute;top:78px;width:100%;text-align:center;font-size:16px;color:#222}
.video-title{left:223px;top:190px;font-family:"Montserrat",Arial,sans-serif;color:var(--white);font-size:29px;line-height:38px}
.video-title strong{font-weight:700;display:block}
.video-title span{font-weight:300;display:block}
.video-copy{left:223px;top:275px;width:260px;font-size:11px;line-height:16px;color:#223}
.video-frame{left:595px;top:131px;width:555px;height:288px;background:radial-gradient(circle at 50% 50%,#5b4f44 0%,#2b2622 55%,#141210 100%)}
.video-frame svg{position:absolute;left:235px;top:100px}

/* social */
.community{top:1844px;height:346px}
.community h2{position:absolute;top:32px;width:100%;font-size:31px}
.events{left:177px;top:146px;width:170px}
.events h4{font-weight:400;font-size:16px;color:#666}
.event{position:relative;margin-top:18px;padding-left:40px}
.event svg{position:absolute;left:0;top:6px}
.event .date{font-size:11px;color:#444}
.event .title{font-size:11px;line-height:15px;color:var(--accent)}
.social{position:absolute;top:126px;width:200px;text-align:center;transform:translateX(-50%)}
.social .dot{width:64px;height:64px;border-radius:50%;background:var(--brand);margin:0 auto}
.social h4{margin-top:10px;font-weight:400;font-size:16px;color:#333}
.social p{margin-top:10px;font-size:11px;line-height:16px;color:var(--muted)}

/* testimonial */
.testimonial-band{top:2190px;height:182px;background:var(--band-grey)}
.portrait{left:206px;top:41px;width:54px;height:56px;background:linear-gradient(160deg,#d7dde2,#a9b3bb)}
.quote{left:286px;top:52px;width:320px;font-size:11px;line-height:15px;font-style:italic;color:#777}
.qmark{font-family:Georgia,serif;font-size:22px;color:#888}
.quote-author{left:537px;top:110px;font-size:12px;color:var(--accent)}
.badge{background:#c9c9c9;border-radius:3px}

/* footer */
.site-footer{top:2372px;height:47px;background:var(--footer)}
.copyright{left:177px;top:17px;font-size:10px;color:#bbb}
.site-footer a{position:absolute;top:14px;font-size:13px;color:#eee;text-decoration:none;font-family:"Montserrat",Arial,sans-serif}
</style>
</head>
<body>

<header class="site-header">
  <div class="abs logo">Logo Here</div>
  <div class="abs login-links">
    <a class="login-link">Login to QUOLT Express</a>
    <a class="login-link">Login to QUOLT Master</a>
  </div>
  <a class="abs enrol">Enrol</a>
</header>

<nav class="main-nav">
  <a class="active" style="left:211px">Home</a>
  <a style="left:288px">Courses</a>
  <a style="left:361px">Fees</a>
  <a style="left:452px">Testimonials</a>
  <a style="left:547px">Agents</a>
  <a style="left:617px">FAQ</a>
  <a style="left:692px">About Us</a>
  <a style="left:791px">Contact Us</a>
</nav>

<section class="hero">
  <h1 class="heading">LOREM IPSUM DOLOR SIT AMET, <span>CONSECTETUR</span><br>NEC ULLAMCORPER DUI</h1>
  <div class="abs hero-photo" role="img" aria-label="Photo of five students studying together at laptops"></div>
</section>

<section class="features">
  <div class="feature" style="left:300px">
    <svg class="feature-icon" viewBox="0 0 80 80" aria-hidden="true">
      <circle cx="40" cy="40" r="37" fill="none" stroke="#fff" stroke-width="3"/>
      <path d="M22 30h24a4 4 0 0 1 4 4v10a4 4 0 0 1-4 4H32l-7 6v-6h-3a4 4 0 0 1-4-4V34a4 4 0 0 1 4-4z" fill="#fff"/>
      <path d="M34 24h24a4 4 0 0 1 4 4v10a4 4 0 0 1-4 4h-2v6l-6-6" fill="none" stroke="#fff" stroke-width="3"/>
    </svg>
    <h3>Communication</h3>
    <p>Nam libero tempore, cum soluta nobis est eligendi optio cumque nihil impedit quo minus id quod maxime placeat facere possimus, omnis dolor repellendus.</p>
    <div class="dots">●●●</div>
  </div>
  <div class="feature" style="left:605px">
    <svg class="feature-icon" viewBox="0 0 80 80" aria-hidden="true">
      <circle cx="40" cy="40" r="37" fill="none" stroke="#fff" stroke-width="3"/>
      <path d="M27 20h20l8 8v32H27z" fill="#fff"/>
      <path d="M47 20v8h8" fill="none" stroke="#3276b5" stroke-width="2"/>
    </svg>
    <h3>Review after class</h3>
    <p>Cum soluta nobis est eligendi optio cumque nihil impedit quo minus id quod maxime placeat facere possimus, omnis voluptas assumenda est, omnis dolor repellendus.</p>
    <div class="dots">●●●</div>
  </div>
  <div class="feature" style="left:905px">
    <svg class="feature-icon" viewBox="0 0 80 80" aria-hidden="true">
      <circle cx="40" cy="40" r="37" fill="none" stroke="#fff" stroke-width="3"/>
      <path d="M24 38a16 16 0 0 1 28-10" fill="none" stroke="#fff" stroke-width="5"/>
      <path d="M56 20v12H44z" fill="#fff"/>
      <path d="M56 42a16 16 0 0 1-28 10" fill="none" stroke="#fff" stroke-width="5"/>
      <path d="M24 60V48h12z" fill="#fff"/>
    </svg>
    <h3>Total flexibility</h3>
    <p>Et harum quidem rerum facilis est et expedita distinctio. Cumque nihil impedit quo minus id quod maxime placeat facere possimus, omnis dolor repellendus.</p>
    <div class="dots">●●●</div>
  </div>
</section>

<section class="packages">
  <h2 class="heading">LOREM IPSUM DOLOR SIT AMET</h2>
  <p class="intro">Nam libero tempore, cum soluta nobis est eligendi optio cumque nihil impedit quo minus id quod maxime placeat facere possimus, omnis voluptas assumenda est, omnis dolor repellendus. Nam libero tempore, cum soluta</p>
  <div class="vrule" style="left:460px;top:208px;height:100px"></div>
  <div class="vrule" style="left:745px;top:208px;height:100px"></div>
  <div class="package" style="left:310px">
    <h3>Teacher details</h3>
    <p>Lorem ipsum dolor sit amet, consectetur adipiscing elit. Duis mollis metus arcu, nec ullamcorper dui venenatis nec.</p>
    <a class="btn">More Info</a>
  </div>
  <div class="package" style="left:617px">
    <h3>Payment details</h3>
    <p>Lorem ipsum dolor sit amet, consectetur adipiscing elit. Duis mollis metus arcu, nec ullamcorper dui venenatis nec.</p>
    <a class="btn">More Info</a>
  </div>
  <div class="package" style="left:898px">
    <h3>Lesson details</h3>
    <p>Lorem ipsum dolor sit amet, consectetur adipiscing elit. Duis mollis metus arcu, nec ullamcorper dui venenatis nec.</p>
    <a class="btn">More Info</a>
  </div>
</section>

<section class="video-band">
  <h2 class="heading">DOLOR SIT AMET</h2>
  <p class="sub">Lorem ipsum dolor sit amet, consectetur adipiscing elit. Phasellus consectetur,</p>
  <div class="abs video-title"><strong>LOREM IPSUM.</strong><span>DOLOR SIT</span></div>
  <p class="abs video-copy">Lorem ipsum dolor sit amet, consectetur adipiscing elit. Donec faucibus justo non gravida rutrum. Phasellus ac nibh magna. Nam consectetur, risus nec cursus sodales, erat ante</p>
  <div class="abs video-frame" role="img" aria-label="Video still of a group meeting around a table, seen from above">
    <svg width="86" height="90" viewBox="0 0 86 90" aria-hidden="true">
      <path d="M43 3l38 22v40L43 87 5 65V25z" fill="#fff" opacity=".92"/>
      <path d="M34 28l24 17-24 17z" fill="#333"/>
    </svg>
  </div>
</section>

<section class="community">
  <h2 class="heading">LOREM IPSUM DOLOR SIT AMET</h2>
  <div class="abs events">
    <h4>Upcoming Events</h4>
    <div class="event">
      <svg width="26" height="24" viewBox="0 0 26 24" aria-hidden="true">
        <rect x="1" y="3" width="24" height="20" fill="none" stroke="#aaa" stroke-width="2"/>
        <path d="M1 9h24M7 1v5M19 1v5M6 13h3M12 13h3M18 13h3M6 18h3M12 18h3" stroke="#aaa" stroke-width="2"/>
      </svg>
      <div class="date">22-11-2013</div>
      <div class="title">Following the Paths<br>of the Pages</div>
    </div>
  </div>
  <div class="vrule" style="left:353px;top:104px;height:230px"></div>
  <div class="vrule" style="left:581px;top:104px;height:230px"></div>
  <div class="vrule" style="left:806px;top:104px;height:230px"></div>
  <div class="social" style="left:465px">
    <div class="dot"></div>
    <h4>Friendwall</h4>
    <p>Lorem ipsum dolor sit amet, consectetur adipiscing elit. Duis mollis metus arcu, nec ullamcorper dui venenatis nec.</p>
  </div>
  <div class="social" style="left:690px">
    <div class="dot"></div>
    <h4>Chirplo</h4>
    <p>Lorem ipsum dolor sit amet, consectetur adipiscing elit. Duis mollis metus arcu, nec ullamcorper dui venenatis nec.</p>
  </div>
  <div class="social" style="left:912px">
    <div class="dot"></div>
    <h4>Talqo</h4>
    <p>Lorem ipsum dolor sit amet, consectetur adipiscing elit. Duis mollis metus arcu, nec ullamcorper dui venenatis nec.</p>
  </div>
</section>

<section class="testimonial-band">
  <div class="abs portrait" role="img" aria-label="Portrait photo of the quoted student"></div>
  <div class="abs qmark" style="left:276px;top:34px">“</div>
  <p class="abs quote">Curabitur a dolor sit amet mi vulputate dignissim. Morbi quis ante mauris. Nunc sapien felis, vestibulum facilisis accumsan at, lacinia ac massa.</p>
  <div class="abs qmark" style="left:520px;top:92px">”</div>
  <div class="abs quote-author">Throughout</div>
  <div class="vrule" style="left:668px;top:24px;height:110px;background:#d5d5d5"></div>
  <div class="abs badge" style="left:700px;top:52px;width:62px;height:22px"></div>
  <div class="abs badge" style="left:846px;top:46px;width:36px;height:32px"></div>
  <div class="abs badge" style="left:962px;top:42px;width:28px;height:32px"></div>
  <div class="abs badge" style="left:700px;top:112px;width:58px;height:20px"></div>
</section>

<footer class="site-footer">
  <div class="abs copyright">© 2014 tutorvane.example, All Rights Reserved</div>
  <a style="left:582px">Home</a>
  <a style="left:652px">Courses</a>
  <a style="left:740px">Fees</a>
  <a style="left:800px">FAQ</a>
  <a style="left:862px">About Us</a>
  <a style="left:954px">Contact Us</a>
</footer>

</body>
</html>
```